Re design current site.

Redesign of the current site. Like current design But I don't own it so I need a custom design similar to the current one. Want the model pictures to be shown off as they currently do on the home page I want to show off contact info make it very noticeable and readable.
Target Market(s)
Males age 30-60
Number of Pages Required
1 page
Requirements
Must have
- Must show off model pictures on the page. Must show contact info easy to read easy to find.

```html
<!DOCTYPE html>
<html lang="en">
<head>
<meta charset="utf-8">
<title>Velora Models</title>
<link href="https://fonts.googleapis.com/css2?family=Poppins:wght@300;400;600;700;800&family=Dancing+Script:wght@700&display=swap" rel="stylesheet">
<style>
:root{
  --page:#2e2431;
  --header-dark:#3a2c3a;
  --header-light:#8b7890;
  --nav:#b73232;
  --panel:#d8d5d9;
  --violet:#5a12e6;
  --teal:#1dd6b0;
  --plum:#8f3c9b;
  --magenta:#a52ad1;
  --cta:#b51fd8;
  --aqua:#1ef2d8;
  --red:#e8202a;
  --yellow:#f4e01a;
  --ink:#2a2a2a;
  --label:#f2f2f2;
  --white:#ffffff;
}
*{box-sizing:border-box;margin:0;padding:0}
html,body{width:857px;height:1200px;overflow:hidden}
body{position:relative;background:var(--page);font-family:"Poppins",sans-serif;color:var(--ink)}
.abs{position:absolute}

.hero{left:0;top:0;width:857px;height:99px;background:linear-gradient(100deg,var(--header-light) 0%,var(--header-dark) 45%,var(--header-dark) 60%,var(--header-light) 100%)}
.brand{left:0;top:14px;width:857px;text-align:center;color:var(--white);font-weight:400;font-size:25px;letter-spacing:1px}
.brand-mark{display:inline-block;width:14px;height:14px;background:var(--white);margin-right:10px;vertical-align:2px}
.tagline{left:0;top:64px;width:857px;text-align:center;color:#e9dcef;font-family:"Dancing Script",cursive;font-size:21px}

.nav{left:0;top:99px;width:857px;height:27px;background:var(--nav)}
.nav a{position:absolute;top:7px;color:var(--white);font-size:9px;text-decoration:none;transform:translateX(-50%)}

.intro{left:107px;top:137px;width:438px;height:200px;background:var(--panel);padding:20px 12px;text-align:center;font-size:14.5px;font-weight:300;line-height:26.8px}
.intro strong,.agency strong{color:var(--plum);font-weight:700}
.contact{left:545px;top:137px;width:205px;height:200px;background:linear-gradient(100deg,var(--violet),var(--teal))}
.contact-row{position:absolute;left:26px;color:var(--white);font-weight:600;display:flex;align-items:center}
.contact-phone{top:30px;font-size:15.5px}
.contact-mail{top:70px;font-size:10px}
.contact-row svg{margin-right:18px}
.call-btn{left:38px;top:134px;width:131px;height:32px;background:var(--plum);color:var(--aqua);font-family:"Dancing Script",cursive;font-size:17px;text-align:center;line-height:32px}

.model{position:absolute;background:var(--label)}
.model .photo{width:100%}
.model .name{height:21px;padding-left:8px;font-size:9.5px;line-height:21px;color:var(--ink)}

.dots{left:0;width:857px;display:flex;justify-content:center;gap:4px}
.dots span{width:8px;height:8px;border-radius:50%;background:var(--white)}
.dots span.on{background:var(--magenta)}
.book-btn{left:363px;top:583px;width:131px;height:32px;background:var(--aqua);color:var(--red);font-family:"Dancing Script",cursive;font-size:17px;text-align:center;line-height:32px}

.extras{left:107px;top:840px;width:211px;height:206px;background:var(--violet);text-align:center;font-weight:800;font-size:14.5px;line-height:24.5px;padding-top:13px}
.extras .couple{color:var(--red);padding:0 16px}
.extras .clips{color:var(--aqua);margin-top:17px;padding:0 10px}
.agency{left:318px;top:840px;width:432px;height:206px;background:var(--panel);text-align:center;font-size:14.5px;font-weight:300;line-height:20px;padding:25px 18px 0}
.agency .areas{color:var(--yellow);font-weight:800}
.see-btn{display:inline-block;margin-top:17px;background:var(--cta);color:var(--white);font-size:9.5px;font-weight:400;padding:0 13px;height:26px;line-height:26px}

.news-title{left:0;top:1056px;width:857px;text-align:center;color:var(--white);font-size:12px;font-weight:300}
.news-input{left:344px;top:1075px;width:176px;height:27px;background:var(--white);font-size:7px;color:#888;padding-left:7px;line-height:27px}
.news-btn{left:386px;top:1105px;width:86px;height:26px;background:#f2f2f2;color:#888;font-size:10px;text-align:center;line-height:26px}

.footer{left:0;top:1146px;width:857px;height:54px;background:var(--plum);color:var(--white);text-align:center;font-size:10px;font-weight:600;line-height:54px}
</style>
</head>
<body>
<header class="hero abs" role="img" aria-label="Dim bedroom photograph behind the header"></header>
<div class="brand abs"><span class="brand-mark"></span>VELORA MODELS</div>
<div class="tagline abs">Treat Yourself and we'll Treat you</div>

<nav class="nav abs">
  <a style="left:210px">HOME</a>
  <a style="left:294px">BOOKINGS</a>
  <a style="left:379px">RATES</a>
  <a style="left:458px">MODELS</a>
  <a style="left:554px">EMPLOYMENT</a>
  <a style="left:642px">LINKS</a>
</nav>

<section class="intro abs">
  <p><strong>VeloraModels Concierge Service</strong> allows clients to request VeloraModels to search for models in the location you plan on traveling to. We will search and find attractive models for the dates requested. We also verify they are interested in the service you expect/request and that the pictures we have are recent and real.</p>
</section>
<aside class="contact abs">
  <div class="contact-row contact-phone">
    <svg width="16" height="16" viewBox="0 0 24 24"><path fill="#fff" d="M6.6 10.8c1.4 2.8 3.8 5.1 6.6 6.6l2.2-2.2c.3-.3.7-.4 1-.2 1.1.4 2.3.6 3.6.6.6 0 1 .4 1 1V20c0 .6-.4 1-1 1C10.6 21 3 13.4 3 4c0-.6.4-1 1-1h3.5c.6 0 1 .4 1 1 0 1.3.2 2.5.6 3.6.1.3 0 .7-.2 1z"/></svg>
    <span style="margin-left:22px">555-014-2290</span>
  </div>
  <div class="contact-row contact-mail">
    <svg width="20" height="14" viewBox="0 0 20 14"><rect x="0.5" y="0.5" width="19" height="13" fill="none" stroke="#fff"/><path d="M0.5 0.5 10 8 19.5 0.5M0.5 13.5 7.5 6.5M19.5 13.5 12.5 6.5" fill="none" stroke="#fff"/></svg>
    <span>hello@veloramodels.com</span>
  </div>
  <div class="call-btn abs">Call Now</div>
</aside>

<div class="model" style="left:122px;top:362px;width:195px">
  <div class="photo" role="img" aria-label="Model photo, striped top outdoors by green hedge" style="height:173px;background:linear-gradient(160deg,#4f6b2a,#8ea05a 60%,#c8b8c8)"></div>
  <div class="name">Lana Vee</div>
</div>
<div class="model" style="left:330px;top:362px;width:194px">
  <div class="photo" role="img" aria-label="Model photo in black outfit against dark background" style="height:173px;background:linear-gradient(180deg,#0d0d0d,#2a1a1a 70%,#6a3a3a)"></div>
  <div class="name">Sienna Rose</div>
</div>
<div class="model" style="left:538px;top:362px;width:194px">
  <div class="photo" role="img" aria-label="Model selfie in pink top" style="height:173px;background:linear-gradient(180deg,#e9d9c8,#dca0b0 55%,#d8327a)"></div>
  <div class="name">Daisy</div>
</div>

<div class="dots abs" style="top:570px"><span class="on"></span><span></span><span></span><span></span></div>
<div class="book-btn abs">Book Now</div>
<div class="dots abs" style="top:623px"><span></span><span></span><span class="on"></span><span></span></div>

<div class="model" style="left:125px;top:642px;width:187px">
  <div class="photo" role="img" aria-label="Model portrait in grey t-shirt" style="height:167px;background:linear-gradient(180deg,#c9b6a8,#9c8a80 60%,#8a8a8a)"></div>
  <div class="name">Jade</div>
</div>
<div class="model" style="left:335px;top:642px;width:187px">
  <div class="photo" role="img" aria-label="Model portrait with curly hair" style="height:167px;background:linear-gradient(180deg,#3a2a28,#c89a98 55%,#d8b8c0)"></div>
  <div class="name">Ember</div>
</div>
<div class="model" style="left:546px;top:642px;width:187px">
  <div class="photo" role="img" aria-label="Model mirror selfie in striped skirt" style="height:167px;background:linear-gradient(180deg,#d8cfc0,#8a6a58 55%,#3a3030)"></div>
  <div class="name">Katia</div>
</div>

<section class="extras abs">
  <p class="couple">Male &amp; female couple available as well.</p>
  <p class="clips">Custom clips and videos available for sale!</p>
</section>
<section class="agency abs">
  <p><strong>VeloraModels Escorts Agency</strong> that offers the best companionship in the <span class="areas">Miami, Fort Lauderdale, &amp; West Palm Beach</span> areas. Whether you are looking for companions/call girls for a business meeting or if you are just visiting the South Florida area for a short period of time.</p>
  <span class="see-btn">Click Here to See Our Models</span>
</section>

<div class="news-title abs">Join our Newsletter</div>
<div class="news-input abs">Enter your email</div>
<div class="news-btn abs">Subscribe</div>

<footer class="footer abs">Velora Models Escort Agency, Inc. 2017</footer>
</body>
</html>
```